Mandala-like Graphic for Ecosystem of Well-Being

I have created a simple graphic for a framework I use with clients and potential clients. I would like it to look more polished, professional, and customized. (As opposed to non-graphic designer created it on Canva or Powrepoint) I would like to possibly integrate my brand colors---or one of my brand colors. https://tintcrate.net/color-palette-5817/ The dark blue is the one to definitely use. I do not want it looking to feminine. I do want different colors for the 5 elements: Purpose, Mental, Physical, Emotional, Social.

Target Market(s)

Working professionals.

Font styles to use
Serif
Other font styles liked:
• Playfair Display

Requirements
Must have
• 4 Overlapping circles with one circle in center that says Purpose
Other 4 circles labeled Physical, Emotional, Mental, Social
Mandala-like design

**I added an attachment with colors I use when marketing this course.**
Nice to have
• Playfair Display font

```html
<!DOCTYPE html>
<html lang="en">
<head>
<meta charset="utf-8">
<title>Ecosystem of Well-Being</title>
<link rel="stylesheet" href="https://fonts.googleapis.com/css2?family=Playfair+Display:wght@700;900&display=swap">
<style>
  :root {
    --canvas: #ffffff;
    --white: #ffffff;
    --physical-fill: #cc3785;
    --physical-ring: #f46db4;
    --mental-fill: #6ea611;
    --mental-ring: #ade24c;
    --emotional-fill: #e80000;
    --emotional-ring: #ff5858;
    --social-fill: #ff8a00;
    --social-ring: #ffb35e;
    --purpose-fill: #255587;
    --purpose-ring: #5b9ee2;
  }
  html, body {
    margin: 0;
    padding: 0;
    overflow: hidden;
    background: var(--canvas);
  }
  .wellbeing-canvas {
    position: relative;
    width: 1200px;
    height: 1000px;
    overflow: hidden;
    background: var(--canvas);
  }
  .wellbeing-mandala {
    display: block;
    width: 1200px;
    height: 1000px;
  }
  .petal-outline { fill: none; stroke-width: 7; }
  .element-ring { fill: none; stroke-width: 8; }
  .element-label {
    font-family: "Playfair Display", Georgia, serif;
    font-weight: 900;
    font-size: 44px;
    fill: var(--white);
    text-anchor: middle;
    letter-spacing: 0.5px;
  }
  .icon-line {
    fill: none;
    stroke: var(--white);
    stroke-width: 6;
    stroke-linecap: round;
    stroke-linejoin: round;
  }
  .icon-solid { fill: var(--white); }
  .physical .element-fill { fill: var(--physical-fill); }
  .physical .element-ring { stroke: var(--physical-ring); }
  .mental .element-fill { fill: var(--mental-fill); }
  .mental .element-ring { stroke: var(--mental-ring); }
  .emotional .element-fill { fill: var(--emotional-fill); }
  .emotional .element-ring { stroke: var(--emotional-ring); }
  .social .element-fill { fill: var(--social-fill); }
  .social .element-ring { stroke: var(--social-ring); }
  .purpose .element-fill { fill: var(--purpose-fill); }
  .purpose .element-ring { stroke: var(--purpose-ring); stroke-width: 11; }
  .purpose .inner-ring { fill: none; stroke: var(--white); stroke-width: 5; }
</style>
</head>
<body>
<main class="wellbeing-canvas">
  <svg class="wellbeing-mandala" viewBox="0 0 1200 1000" role="img" aria-label="Ecosystem of Well-Being: Purpose at the centre of Physical, Mental, Emotional and Social">
    <defs>
      <linearGradient id="grad-top" x1="0" y1="0" x2="1" y2="0">
        <stop offset="0" stop-color="#f46db4"/><stop offset="1" stop-color="#c9d44a"/>
      </linearGradient>
      <linearGradient id="grad-left" x1="0" y1="0" x2="0" y2="1">
        <stop offset="0" stop-color="#f46db4"/><stop offset="1" stop-color="#ff5858"/>
      </linearGradient>
      <linearGradient id="grad-right" x1="0" y1="0" x2="0" y2="1">
        <stop offset="0" stop-color="#ade24c"/><stop offset="1" stop-color="#ffb35e"/>
      </linearGradient>
      <linearGradient id="grad-bottom" x1="0" y1="0" x2="1" y2="0">
        <stop offset="0" stop-color="#ff5858"/><stop offset="1" stop-color="#ffb35e"/>
      </linearGradient>
    </defs>

    <!-- outer petals -->
    <g class="petals">
      <circle class="petal-outline" cx="600" cy="265" r="188" stroke="url(#grad-top)"/>
      <circle class="petal-outline" cx="370" cy="500" r="188" stroke="url(#grad-left)"/>
      <circle class="petal-outline" cx="830" cy="500" r="188" stroke="url(#grad-right)"/>
      <circle class="petal-outline" cx="600" cy="735" r="188" stroke="url(#grad-bottom)"/>
    </g>

    <!-- physical -->
    <g class="element physical">
      <circle class="element-fill" cx="435" cy="335" r="180"/>
      <circle class="element-ring" cx="435" cy="335" r="197"/>
      <text class="element-label" x="430" y="286">PHYSICAL</text>
      <g class="element-icon">
        <circle class="icon-line" cx="428" cy="352" r="46"/>
        <rect class="icon-solid" x="405" y="328" width="44" height="36" rx="9"/>
        <rect class="icon-solid" x="408" y="360" width="22" height="36" rx="4"/>
      </g>
    </g>

    <!-- mental -->
    <g class="element mental">
      <circle class="element-fill" cx="765" cy="335" r="180"/>
      <circle class="element-ring" cx="765" cy="335" r="197"/>
      <text class="element-label" x="770" y="286">MENTAL</text>
      <g class="element-icon">
        <path class="icon-line" d="M768 306 C740 296 726 318 733 334 C718 346 724 370 740 372 C744 390 762 392 768 384 Z"/>
        <path class="icon-line" d="M772 306 C800 296 814 318 807 334 C822 346 816 370 800 372 C796 390 778 392 772 384 Z"/>
        <path class="icon-line" d="M748 340 h10 M782 340 h10 M750 356 h8 M782 356 h8"/>
      </g>
    </g>

    <!-- emotional -->
    <g class="element emotional">
      <circle class="element-fill" cx="435" cy="665" r="180"/>
      <circle class="element-ring" cx="435" cy="665" r="197"/>
      <text class="element-label" x="422" y="743">EMOTIONAL</text>
      <g class="element-icon">
        <path class="icon-solid" d="M422 695 L378 652 C360 634 372 604 398 606 C410 607 418 614 422 622 C426 614 434 607 446 606 C472 604 484 634 466 652 Z"/>
        <path class="icon-line" stroke="#e80000" d="M368 656 h32 l8 -16 l10 34 l10 -50 l10 32 h40" style="stroke:#e80000"/>
        <path class="icon-line" d="M368 660 h30 M458 660 h20"/>
      </g>
    </g>

    <!-- social -->
    <g class="element social">
      <circle class="element-fill" cx="765" cy="665" r="180"/>
      <circle class="element-ring" cx="765" cy="665" r="197"/>
      <text class="element-label" x="768" y="743">SOCIAL</text>
      <g class="element-icon">
        <path class="icon-line" d="M728 606 h78 a10 10 0 0 1 10 10 v60 l8 16 l-20 -8 h-76 a10 10 0 0 1 -10 -10 v-58 a10 10 0 0 1 10 -10 Z"/>
        <circle class="icon-solid" cx="745" cy="628" r="8"/>
        <circle class="icon-solid" cx="785" cy="628" r="8"/>
        <path class="icon-solid" d="M731 658 a14 14 0 0 1 28 0 Z M771 658 a14 14 0 0 1 28 0 Z"/>
        <circle class="icon-solid" cx="765" cy="642" r="10"/>
        <path class="icon-solid" d="M746 672 a19 19 0 0 1 38 0 Z"/>
      </g>
    </g>

    <!-- purpose -->
    <g class="element purpose">
      <circle class="element-ring" cx="600" cy="495" r="149"/>
      <circle fill="#ffffff" cx="600" cy="495" r="143"/>
      <circle class="element-fill" cx="600" cy="495" r="132"/>
      <text class="element-label" x="600" y="538" style="font-size:46px">PURPOSE</text>
      <g class="element-icon">
        <circle class="icon-line" cx="600" cy="450" r="36"/>
        <circle class="icon-line" cx="600" cy="450" r="21"/>
        <circle class="icon-solid" cx="600" cy="450" r="7"/>
        <path class="icon-line" d="M600 450 L640 410"/>
        <path class="icon-solid" d="M632 404 l12 -12 l2 12 l12 2 l-12 12 l-12 -2 Z"/>
      </g>
    </g>
  </svg>
</main>
</body>
</html>
```